Email Template For Tennis School (PSD only)

Big bright and cheery emails to engage customers to book tennis competitions or rejoin the tennis school:

-
Output:
1 LAYOUT and 4 EMAILS = 4 PSD designs to be delivered.
(No need to do 4 different layouts, 1 will do)
-
INSPIRATIONAL DESIGNS
http://na1.mailvault-store1.example/?u=5b2e91c4f07a3d8e6c1b2a9f4&id=1c7e4b9a20
http://na1.mailvault-store2.example/?u=8e14c7b2a09d5f3e6a7b1c4d2&id=94b1d7e3a6
http://na2.mailvault-store1.example/?u=f2a7d19c4e6b03a8d5c2e7b14&id=7a3c9e1f5b

1. Adult tennis competition including singles and doubles competitions. Singles competition is 1 hour while doubles is 2 hours over 10 weeks.

2. Junior mixed format competition which includes a set of singles for each player and a set of doubles. Competition is held over 10 weeks for 2 hours per week.

3. QRV Court Nation Sky Aces competition held over 10 weeks with variable times depending on the format. (Junior competition)

4. Engage lapsed customers with a coupon. Lapsed customers are those who haven't participated in over 12 months.

The emails can all be based on the same layout with different copy and artwork.

Please refer to customer site for look and feel:

www.bramcourts.example

Last part of the design:
* Please use more males in your designs as 90% of participants are males
* Use this heading somewhere "Reply to this email for queries or call 0493 627 159"
* Include a small Burgerwell's logo and copy "Proudly Sponsored by Burgerwells Ashcombe & Pinebrook".
* Please incorporate the following copy:

Location: Wexley Only
Begins: Thursday 17th January 2014
Ends: Thursday 28th March 2014 (Weather permitting, if the competition is washed out one week it will continue on for an additional week).
Times:
Thursday Wexley: 6:30pm-7:30pm Singles Competition
Thursday Wexley: 7:30pm-9:30pm
Format:
Thursday Night Singles Competition - 6:30pm
1 hour of singles play.  Each player competes in a 1 hour singles match and plays as many games as possible during this time.  Round robin format.
Thursday Night Adult Competition - 7:30pm
Teams can be mens, ladies or mixed.  2 players per team, each player has one set of singles & doubles.  2 hour duration.
Entries Close:
Wednesday 16th January 2013
The adult competition caters for all standards from Beginners to Advanced.

• 1. BramCourts.example logo must appear in email
2. A "Book Now" button - obvious in layout
3. Bright cheery pictures which inspire people to buy.
4. Artwork must suit target market.

```html
<!DOCTYPE html>
<html lang="en">
<head>
<meta charset="utf-8">
<title>Adult Competition – BramCourts.example</title>
<link href="https://fonts.googleapis.com/css2?family=Open+Sans:wght@400;600;700&display=swap" rel="stylesheet">
<style>
:root{
  --page-blue:#1b5fa6;
  --page-blue-dark:#124a86;
  --sheet:#ffffff;
  --heading-teal:#1e9bbd;
  --link-blue:#2f7fc8;
  --text:#333a44;
  --band-red:#d8241c;
  --cta-red:#e8321d;
  --cta-red-dark:#b81d0f;
  --notice-yellow:#fff200;
  --reply-orange:#f7b02b;
  --bullet:#2f7fc8;
}
*{margin:0;padding:0;box-sizing:border-box}
html,body{width:723px;height:1200px;overflow:hidden}
body{background:linear-gradient(180deg,var(--page-blue) 0%,var(--page-blue-dark) 100%);font-family:"Open Sans",Arial,sans-serif;color:var(--text);position:relative}
.top-links{position:absolute;left:92px;top:8px;font-size:11px;color:#fff}
.top-links span{margin:0 6px}
.sheet{position:absolute;left:92px;top:29px;width:540px;height:1092px;background:var(--sheet)}
.header{position:absolute;left:0;top:0;width:540px;height:136px;background:linear-gradient(135deg,#3a9a3a 0%,#8fcf4a 40%,#2f86c8 100%)}
.header-photo{position:absolute;left:0;top:0;width:540px;height:136px;background:linear-gradient(90deg,rgba(255,255,255,0) 30%,rgba(230,240,250,.35) 100%)}
.brand{position:absolute;left:14px;top:48px;display:flex;align-items:center;gap:8px}
.brand-mark{width:34px;height:34px;border-radius:50%;background:#fff200}
.brand-name{font-size:22px;font-weight:700;color:#fff}
.reply{position:absolute;right:0;top:-29px;width:176px;height:50px;background:var(--reply-orange);color:#fff;font-size:11px;font-weight:600;text-align:center;padding-top:6px;line-height:15px;border-radius:0 0 0 6px}
.phone{position:absolute;right:12px;top:38px;display:flex;align-items:center;gap:8px}
.phone-icon{width:40px;height:40px;border-radius:50%;background:var(--band-red);display:flex;align-items:center;justify-content:center}
.phone-number{background:rgba(255,255,255,.9);color:#1f2a36;font-weight:700;font-size:17px;padding:6px 14px;border-radius:3px}
.sponsor-band{position:absolute;left:0;top:136px;width:540px;height:24px;background:var(--band-red);color:#fff;font-size:12px;font-weight:600;display:flex;align-items:center;justify-content:flex-end;padding-right:14px;gap:8px}
.sponsor-mark{width:18px;height:18px;background:#ffc72c}
.page-title{position:absolute;left:0;top:170px;width:540px;text-align:center;font-size:30px;font-weight:700;color:var(--heading-teal)}
.title-rule{position:absolute;left:60px;top:218px;width:420px;height:2px;background:linear-gradient(90deg,rgba(30,155,189,0),rgba(30,155,189,.5),rgba(30,155,189,0))}
.section-title{position:absolute;left:0;width:540px;text-align:center;font-size:22px;font-weight:700;color:var(--heading-teal)}
.photos{position:absolute;left:17px;width:506px;display:flex;gap:8px}
.photo{flex:1;height:104px}
.details{position:absolute;left:20px;width:272px;list-style:none;font-size:11px;line-height:14px}
.details li{position:relative;padding-left:20px;margin-bottom:9px}
.details li::before{content:"";position:absolute;left:2px;top:4px;width:7px;height:7px;border-radius:50%;background:var(--bullet)}
.details b{color:#1f2a36}
.details .date{color:var(--link-blue)}
.details .note{font-style:italic;color:#555}
.time-box{position:absolute;left:312px;width:210px;height:32px;background:var(--notice-yellow);color:#1f2a36;font-weight:700;font-size:12px;white-space:nowrap;display:flex;align-items:center;justify-content:center}
.book-btn{position:absolute;left:312px;width:210px;height:36px;border-radius:18px;background:linear-gradient(180deg,var(--cta-red),var(--cta-red-dark));color:#fff;font-weight:700;font-size:12px;white-space:nowrap;display:flex;align-items:center;justify-content:center;gap:10px}
.footer{position:absolute;left:92px;top:1130px;width:540px;color:#fff;font-size:11px;line-height:17px}
.footer b{font-weight:700}
.social{position:absolute;right:0;top:4px;display:flex;gap:8px}
.social span{width:28px;height:28px;background:rgba(255,255,255,.85);border-radius:4px}
</style>
</head>
<body>
<div class="top-links">View this newsletter online <span>|</span> Unsubscribe</div>

<div class="sheet">
  <header class="header">
    <div class="header-photo" role="img" aria-label="Bright tennis court scene with a male player mid-swing"></div>
    <div class="brand"><span class="brand-mark"></span><span class="brand-name">BramCourts.example</span></div>
    <div class="reply">Reply to this email for queries<br>or call</div>
    <div class="phone">
      <span class="phone-icon"><svg width="20" height="20" viewBox="0 0 24 24"><path fill="#fff" d="M6.6 10.8a15.1 15.1 0 0 0 6.6 6.6l2.2-2.2c.3-.3.7-.4 1-.2 1.1.4 2.3.6 3.6.6.6 0 1 .4 1 1V20c0 .6-.4 1-1 1C10.6 21 3 13.4 3 4c0-.6.4-1 1-1h3.5c.6 0 1 .4 1 1 0 1.3.2 2.5.6 3.6.1.3 0 .7-.2 1z"/></svg></span>
      <span class="phone-number">0493 627 159</span>
    </div>
  </header>
  <div class="sponsor-band"><span class="sponsor-mark"></span>Proudly Sponsored by Burgerwells Ashcombe &amp; Pinebrook</div>

  <h1 class="page-title">Adult Competition</h1>
  <div class="title-rule"></div>

  <h2 class="section-title" style="top:232px">Night Singles Competition</h2>
  <div class="photos" style="top:270px">
    <div class="photo" role="img" aria-label="Male player serving on a hard court" style="background:linear-gradient(135deg,#4a8fd0,#2d6fb0)"></div>
    <div class="photo" role="img" aria-label="Player hitting a forehand on grass" style="background:linear-gradient(135deg,#5aa04a,#3a7a32)"></div>
    <div class="photo" role="img" aria-label="Player on a clay court" style="background:linear-gradient(135deg,#c0734a,#8a5a3a)"></div>
  </div>
  <ul class="details" style="top:390px">
    <li><b>Location:</b> Wexley Only</li>
    <li><b>Begins:</b> <span class="date">Thursday 17th January 2014</span><br><b>Ends:</b> <span class="date">Thursday 28th March 2014</span><br><span class="note">(Weather permitting, if the competition is washed out one week it will continue on for an additional week)</span></li>
    <li><b>Format:</b><br><span class="date">Thursday Night Singles Competition - 6:30pm</span><br><b>1 hour of singles play.</b> Each player competes in a 1 hour singles match and plays as many games as possible during this time. <b>Round robin format.</b></li>
    <li><b>Entries Close:</b><br><span class="date">Wednesday 16th January 2013</span></li>
  </ul>
  <div class="time-box" style="top:396px">Thursday 6:30 – 7:30pm Wexley</div>
  <div class="book-btn" style="top:440px"><span>7 WEEK TERM $88</span><span>BOOK NOW</span></div>

  <h2 class="section-title" style="top:650px">Night Adult Competition</h2>
  <div class="photos" style="top:688px">
    <div class="photo" role="img" aria-label="Doubles players at the net" style="background:linear-gradient(135deg,#e8c23a,#c49a2a)"></div>
    <div class="photo" role="img" aria-label="Team of players celebrating" style="background:linear-gradient(135deg,#6fb3e0,#3d86c2)"></div>
    <div class="photo" role="img" aria-label="Player holding a racquet" style="background:linear-gradient(135deg,#d8d8d8,#a8a8a8)"></div>
  </div>
  <ul class="details" style="top:808px">
    <li><b>Location:</b> Wexley Only</li>
    <li><b>Begins:</b> <span class="date">Thursday 17th January 2014</span><br><b>Ends:</b> <span class="date">Thursday 28th March 2014</span><br><span class="note">(Weather permitting, if the competition is washed out one week it will continue on for an additional week)</span></li>
    <li><b>Format:</b><br><span class="date">Thursday Night Adult Competition - 7:30pm</span><br><b>Teams can be mens, ladies or mixed.</b> 2 players per team, each player has one set of singles &amp; doubles. <b>2 hour duration.</b></li>
    <li><b>Entries Close:</b><br><span class="date">Wednesday 16th January 2013</span></li>
  </ul>
  <div class="time-box" style="top:814px">Thursday 7:30pm-9:30pm Wexley</div>
  <div class="book-btn" style="top:858px"><span>10 WEEK TERM $120</span><span>BOOK NOW</span></div>
</div>

<footer class="footer">
  <b>© 2013 Bram Hallett School of Tennis</b><br>
  Established 1986. <b>Phone</b> 0493 627 159 <b>Email</b> mail@bramcourts.example
  <div class="social"><span></span><span></span></div>
</footer>
</body>
</html>
```